FixNestly.com Needs a new Design

We need a card design for a new start up company in the Sacramento Ca area called FixNestly.com. We offer homeowners three levels of yearly home maintenance memberships that will help them take care of their yearly home maintenance needs even if there on a fixed income.
Our company tag line is ( We Do The Honey Do's That Other Hubbies Don't Do! )
Updates

Information to be put on card. Martin Kessel Director Phone: 800-374-2916 Fax: 800-374-2916 Address: 4862 Vale Rd Loomis CA 95650

Industry/Entity Type

It Company

```html
<!DOCTYPE html>
<html lang="en">
<head>
<meta charset="utf-8">
<title>FixNestly.com Business Card</title>
<link href="https://fonts.googleapis.com/css2?family=Open+Sans:wght@400;600;700&display=swap" rel="stylesheet">
<style>
  :root {
    --backdrop: #3a3a3c;
    --card-white: #f7f7f5;
    --card-dark: #2b2b2d;
    --card-dark-edge: #1c1c1e;
    --orange: #e2581c;
    --ink: #2e2e2e;
    --ink-soft: #4a4a4a;
    --black: #141414;
  }
  * { box-sizing: border-box; margin: 0; padding: 0; }
  html, body { width: 1200px; height: 900px; overflow: hidden; }
  body {
    background: var(--backdrop);
    font-family: "Open Sans", Arial, sans-serif;
    position: relative;
  }
  .card {
    position: absolute;
    width: 560px;
    height: 320px;
    border-radius: 4px;
    box-shadow: 0 10px 30px rgba(0,0,0,0.45);
    overflow: hidden;
  }
  /* Front: contact side */
  .card-front {
    left: 60px;
    top: 120px;
    background: var(--card-white);
    display: flex;
    align-items: center;
  }
  .front-brand {
    width: 230px;
    height: 100%;
    display: flex;
    align-items: center;
    justify-content: center;
    gap: 10px;
  }
  .brand-dot {
    width: 26px;
    height: 26px;
    border-radius: 50%;
    background: var(--black);
    flex: none;
  }
  .brand-name {
    font-weight: 700;
    font-size: 22px;
    color: var(--orange);
  }
  .front-divider {
    width: 3px;
    height: 200px;
    background: var(--orange);
  }
  .front-details {
    padding-left: 26px;
    color: var(--ink);
  }
  .person-name {
    font-weight: 700;
    font-size: 20px;
    color: var(--orange);
    letter-spacing: 0.5px;
    text-transform: uppercase;
  }
  .person-role {
    font-size: 13px;
    color: var(--ink-soft);
    margin-bottom: 10px;
  }
  .contact-line {
    font-size: 15px;
    line-height: 1.45;
  }
  .contact-label {
    color: var(--orange);
    font-weight: 600;
    text-transform: uppercase;
    margin-right: 6px;
  }
  .address {
    font-size: 15px;
    line-height: 1.45;
    margin-top: 12px;
  }
  .web {
    font-weight: 700;
    font-size: 18px;
    margin-top: 14px;
    color: var(--ink);
  }
  /* Back: brand side */
  .card-back {
    left: 580px;
    top: 460px;
    background: radial-gradient(circle at 50% 50%, #4a4a4c 0%, var(--card-dark) 55%, var(--card-dark-edge) 100%);
    display: flex;
    align-items: center;
    justify-content: center;
  }
  .back-badge {
    width: 250px;
    height: 250px;
    border-radius: 50%;
    background: var(--card-white);
    border: 7px solid var(--orange);
    display: flex;
    align-items: center;
    justify-content: center;
    gap: 10px;
  }
  .back-badge .brand-dot { width: 30px; height: 30px; }
  .back-badge .brand-name { font-size: 26px; }
</style>
</head>
<body>
  <section class="card card-front" aria-label="Business card, contact side">
    <div class="front-brand">
      <span class="brand-dot"></span>
      <span class="brand-name">FixNestly.com</span>
    </div>
    <div class="front-divider"></div>
    <div class="front-details">
      <p class="person-name">Martin Kessel</p>
      <p class="person-role">Director</p>
      <p class="contact-line"><span class="contact-label">Phone</span>(800) 374-2916</p>
      <p class="contact-line"><span class="contact-label">Fax</span>(800) 374-2917</p>
      <p class="contact-line"><span class="contact-label">Email</span>info@FixNestly.com</p>
      <p class="address">4862 Vale Rd<br>Loomis, CA 95650</p>
      <p class="web">FixNestly.com</p>
    </div>
  </section>

  <section class="card card-back" aria-label="Business card, brand side">
    <div class="back-badge">
      <span class="brand-dot"></span>
      <span class="brand-name">FixNestly.com</span>
    </div>
  </section>
</body>
</html>
```